Profesional personal website needs design and business card

I need a business card with my professional name as a logo "Marlo Vitality" for my business. I am a Wellness Coach, consultant and trainer. So it should be professional, wellness oriented and modern.

Target Market(s)

Private clients, governments, corporations. Luxury and high market.

Industry/Entity Type

Health And Wellness

Contact Information for Business Card

Marlo Vitality should be the logo

Colors

Designer to choose colors to be used in the design.

Requirements
Must have
• Marlo Vitality
• Name: Tomás Arribal
• Wellness Coach, Consultant & Trainer.
• Website: www.marlovitality.example
• Phone:
• Spain (+34) 612 480 397
• (USA) +1 (555) 318 2046
Nice to have
• The most important is the design of "Marlo Vitality", as this is going to be my personal brand logo. It should be professional, wellness, high end and actual.
Should not have
• no golds, no baroque style..

```html
<!DOCTYPE html>
<html lang="en">
<head>
<meta charset="UTF-8">
<title>Marlo Vitality — Business Card</title>
<link rel="stylesheet" href="https://fonts.googleapis.com/css2?family=Lato:wght@300;400&display=swap">
<style>
  :root {
    --page-bg: #dedede;
    --card-black: #000000;
    --brand-orange: #ef7a00;
    --ink: #141414;
    --ink-soft: #2a2116;
  }
  * { margin: 0; padding: 0; box-sizing: border-box; }
  html, body {
    width: 849px;
    height: 1200px;
    overflow: hidden;
    background: var(--page-bg);
    font-family: "Lato", Arial, sans-serif;
  }
  .sheet {
    width: 849px;
    height: 1200px;
    display: flex;
    flex-direction: column;
    align-items: center;
    justify-content: center;
    gap: 80px;
  }
  .card {
    width: 640px;
    height: 374px;
    position: relative;
  }
  .card--front {
    background: var(--card-black);
    display: flex;
    align-items: center;
    justify-content: center;
  }
  .brand-name {
    color: var(--brand-orange);
    font-weight: 300;
    font-size: 54px;
    letter-spacing: 1px;
    text-transform: uppercase;
    white-space: nowrap;
  }
  .card--back {
    background: var(--brand-orange);
    color: var(--ink);
  }
  .contact-block {
    position: absolute;
    left: 47px;
    top: 162px;
  }
  .person-name {
    font-weight: 400;
    font-size: 29px;
    line-height: 1.1;
    color: var(--ink);
  }
  .person-role {
    font-weight: 300;
    font-size: 18px;
    margin-top: 4px;
    color: var(--ink-soft);
  }
  .contact-list {
    list-style: none;
    margin-top: 18px;
    font-size: 18px;
    font-weight: 400;
  }
  .contact-item {
    display: flex;
    align-items: center;
    height: 30px;
  }
  .contact-icon {
    width: 22px;
    display: inline-flex;
    align-items: center;
  }
  .contact-icon svg { width: 14px; height: 14px; }
</style>
</head>
<body>
<main class="sheet">
  <section class="card card--front" aria-label="Card front">
    <h1 class="brand-name">Marlo Vitality</h1>
  </section>

  <section class="card card--back" aria-label="Card back">
    <div class="contact-block">
      <h2 class="person-name">Tomás Arribal</h2>
      <p class="person-role">Wellness Coach, Consultant &amp; Trainer</p>
      <ul class="contact-list">
        <li class="contact-item">
          <span class="contact-icon">
            <svg viewBox="0 0 24 24" aria-hidden="true"><path fill="#141414" d="M6.6 10.8a15.1 15.1 0 0 0 6.6 6.6l2.2-2.2a1 1 0 0 1 1-.25 11.4 11.4 0 0 0 3.6.57 1 1 0 0 1 1 1V20a1 1 0 0 1-1 1A17 17 0 0 1 3 4a1 1 0 0 1 1-1h3.5a1 1 0 0 1 1 1c0 1.25.2 2.45.57 3.57a1 1 0 0 1-.25 1z"/></svg>
          </span>
          Spain -&nbsp; (+34) 612 480 397
        </li>
        <li class="contact-item">
          <span class="contact-icon"></span>
          USA - +1 (555) 318 2046
        </li>
        <li class="contact-item">
          <span class="contact-icon">
            <svg viewBox="0 0 24 24" aria-hidden="true" fill="none" stroke="#141414" stroke-width="1.6"><circle cx="12" cy="12" r="9.5"/><ellipse cx="12" cy="12" rx="4.2" ry="9.5"/><line x1="2.5" y1="12" x2="21.5" y2="12"/><path d="M4 7h16M4 17h16"/></svg>
          </span>
          www.marlovitality.example
        </li>
      </ul>
    </div>
  </section>
</main>
</body>
</html>
```